The Lantern Guide

I am a life coach specializing in helping people with depression and bipolar disorder. I would like a nice, fun design for a business card.

```html
<!DOCTYPE html>
<html lang="en">
<head>
<meta charset="utf-8">
<title>The Lantern Guide – Business Card</title>
<link href="https://fonts.googleapis.com/css2?family=Montserrat:wght@500;600;700&family=Arimo:wght@400&display=swap" rel="stylesheet">
<style>
  :root {
    --navy: #1d4d6e;
    --orange: #f0901e;
    --sky: #5bb5e5;
    --ink: #2a3440;
    --card: #ffffff;
    --backdrop: #e9eef2;
    --rule: #b9c3cc;
  }
  * { box-sizing: border-box; margin: 0; padding: 0; }
  html, body {
    width: 1200px; height: 900px; overflow: hidden;
    background: var(--backdrop);
  }
  .card {
    position: absolute;
    left: 150px; top: 190px;
    width: 900px; height: 520px;
    background: var(--card);
    border-radius: 22px;
    overflow: hidden;
    box-shadow: 0 12px 36px rgba(30, 60, 90, 0.18);
  }
  .brand {
    position: absolute;
    left: 0; top: 0;
    width: 480px; height: 440px;
    display: flex; flex-direction: column; align-items: center; justify-content: center;
    text-align: center;
  }
  .brand-dot {
    width: 120px; height: 120px; border-radius: 50%;
    background: var(--sky);
    margin-bottom: 30px;
  }
  .brand-name {
    font-family: 'Montserrat', sans-serif;
    font-weight: 600;
    font-size: 36px;
    color: var(--navy);
    letter-spacing: 0.5px;
    text-transform: uppercase;
  }
  .brand-tagline {
    margin-top: 12px;
    font-family: 'Montserrat', sans-serif;
    font-weight: 500;
    font-size: 17px;
    line-height: 1.4;
    color: var(--navy);
    text-transform: uppercase;
    letter-spacing: 0.4px;
  }
  .divider {
    position: absolute;
    left: 478px; top: 78px;
    width: 1.5px; height: 310px;
    background: var(--rule);
  }
  .contact {
    position: absolute;
    left: 524px; top: 136px;
  }
  .person-name {
    font-family: 'Montserrat', sans-serif;
    font-weight: 700;
    font-size: 32px;
    color: var(--navy);
    text-transform: uppercase;
  }
  .person-title {
    font-family: 'Montserrat', sans-serif;
    font-weight: 500;
    font-size: 21px;
    color: var(--orange);
    letter-spacing: 2px;
    text-transform: uppercase;
    margin-top: 2px;
  }
  .details { list-style: none; margin-top: 32px; }
  .details li {
    display: flex; align-items: flex-start;
    font-family: 'Arimo', sans-serif;
    font-size: 19px; line-height: 1.35;
    color: var(--ink);
    margin-bottom: 6px;
  }
  .details svg { width: 18px; height: 18px; margin: 3px 12px 0 0; flex: none; fill: var(--orange); }
  .wave { position: absolute; left: 0; bottom: 0; width: 900px; height: 90px; }
</style>
</head>
<body>
  <div class="card">
    <div class="brand">
      <div class="brand-dot"></div>
      <div class="brand-name">The Lantern Guide</div>
      <div class="brand-tagline">Helping people with depression<br>and bipolar disorder</div>
    </div>

    <div class="divider"></div>

    <div class="contact">
      <div class="person-name">Paul Hendry</div>
      <div class="person-title">Managing Director</div>
      <ul class="details">
        <li>
          <svg viewBox="0 0 24 24" aria-hidden="true"><path d="M6.6 10.8a15.1 15.1 0 0 0 6.6 6.6l2.2-2.2c.3-.3.7-.4 1-.2 1.1.4 2.3.6 3.6.6.6 0 1 .4 1 1V20c0 .6-.4 1-1 1A17 17 0 0 1 3 4c0-.6.4-1 1-1h3.5c.6 0 1 .4 1 1 0 1.3.2 2.5.6 3.6.1.3 0 .7-.2 1z"/></svg>
          555.014.2287
        </li>
        <li>
          <svg viewBox="0 0 24 24" aria-hidden="true"><path d="M2 5h20v14H2z M2 5l10 8 10-8" fill="none" stroke="#f0901e" stroke-width="0"/><path d="M2 5h20v2l-10 7L2 7z"/><path d="M2 9l10 7 10-7v10H2z"/></svg>
          paul@thelanternguide.com
        </li>
        <li>
          <svg viewBox="0 0 24 24" aria-hidden="true"><path d="M12 2a7 7 0 0 0-7 7c0 5 7 13 7 13s7-8 7-13a7 7 0 0 0-7-7zm0 9.5a2.5 2.5 0 1 1 0-5 2.5 2.5 0 0 1 0 5z"/></svg>
          <span>PO Box 41, Alder Falls, PA 18990<br>Paul Hendry</span>
        </li>
      </ul>
    </div>

    <svg class="wave" viewBox="0 0 900 90" preserveAspectRatio="none" aria-hidden="true">
      <path d="M0 40 C 180 70, 420 50, 600 30 S 820 8, 900 8 L 900 22 C 800 22, 700 38, 600 48 S 250 80, 0 52 Z" fill="var(--orange)"/>
      <path d="M0 54 C 250 84, 480 62, 640 42 S 840 22, 900 24 L 900 90 L 0 90 Z" fill="var(--navy)"/>
    </svg>
  </div>
</body>
</html>
```